Flyer Design Project

We are a restaurant delivery service. We deliver from a variety of restaurants. We are looking for a small flyer that we will put on the front desk at a restaurant that says "We Deliver!" Include our website trovaloopcourier.com and phone number 833-9 Gem Lamp! We would like the emphasis to be on ordering online. The flyer size should be 4.25" x 5.5".

```html
<!DOCTYPE html>
<html lang="en">
<head>
<meta charset="utf-8">
<title>Trovaloop Courier Flyer</title>
<link rel="stylesheet" href="https://fonts.googleapis.com/css2?family=Arimo:wght@700&display=swap">
<style>
  :root {
    --page: #ffffff;
    --brand-red: #a30b0b;
    --ink-dark: #3a2a1a;
    --band-yellow: #fec701;
    --band-edge: #2a2c3a;
    --wall-light: #ecece4;
    --wall-mid: #d9d8cd;
    --wall-dark: #a9a79c;
    --rule: #3a2a1a;
  }
  * { margin: 0; padding: 0; box-sizing: border-box; }
  html, body {
    width: 1200px;
    height: 1000px;
    overflow: hidden;
    background: var(--page);
    font-family: "Arimo", Arial, sans-serif;
  }
  .flyer {
    position: absolute;
    left: 252px;
    top: 50px;
    width: 696px;
    height: 900px;
    overflow: hidden;
  }
  .hero-photo {
    position: absolute;
    inset: 0;
    background:
      radial-gradient(ellipse 70% 55% at 45% 40%, var(--wall-light) 0%, var(--wall-mid) 60%, var(--wall-dark) 100%);
  }
  .headline {
    position: absolute;
    left: 0;
    right: 0;
    top: 150px;
    text-align: center;
    color: var(--brand-red);
    font-weight: 700;
    font-size: 72px;
    line-height: 1;
  }
  .order-online {
    position: absolute;
    left: 0;
    right: 0;
    top: 245px;
    text-align: center;
    color: var(--ink-dark);
    font-weight: 700;
    font-size: 30px;
    line-height: 1;
  }
  .brand-name {
    position: absolute;
    left: 0;
    right: 0;
    top: 430px;
    text-align: center;
    color: var(--brand-red);
    font-weight: 700;
    font-size: 58px;
    line-height: 1;
    letter-spacing: -0.5px;
  }
  .contact-band {
    position: absolute;
    left: 0;
    bottom: 0;
    width: 696px;
    height: 150px;
  }
  .contact-band svg {
    position: absolute;
    inset: 0;
  }
  .website {
    position: absolute;
    left: 0;
    right: 0;
    top: 30px;
    text-align: center;
    color: var(--brand-red);
    font-weight: 700;
    font-size: 31px;
  }
  .divider {
    position: absolute;
    left: 143px;
    width: 410px;
    top: 76px;
    height: 1px;
    background: var(--rule);
  }
  .phone {
    position: absolute;
    left: 0;
    right: 0;
    top: 87px;
    text-align: center;
    color: var(--brand-red);
    font-weight: 700;
    font-size: 32px;
  }
</style>
</head>
<body>
  <div class="flyer">
    <div class="hero-photo" role="img" aria-label="Photo of a white-gloved waiter's hand holding a silver serving tray against a soft grey wall"></div>
    <h1 class="headline">We Deliver!</h1>
    <p class="order-online">Order online anytime</p>
    <div class="brand-name">Trovaloop Courier</div>
    <div class="contact-band">
      <svg width="696" height="150" viewBox="0 0 696 150" aria-hidden="true">
        <path d="M0 50 Q348 -45 696 50 L696 150 L0 150 Z" fill="var(--band-yellow)"/>
        <path d="M0 50 Q348 -45 696 50" fill="none" stroke="var(--band-edge)" stroke-width="5"/>
      </svg>
      <div class="website">trovaloopcourier.com</div>
      <div class="divider"></div>
      <div class="phone">Phone : 833-9 Gem Lamp!</div>
    </div>
  </div>
</body>
</html>
```